Broschüre für Mode und Accessoire Label
Zielgruppe
Für unser neues Label Lunavelle Rare Hair Jewellery sind wir auf der Suche eines Designers für Layout und Design einer Händlerbroschüre. Zielgruppen sind Retailpartner (stationäre und ecommerce Händler aus den unterchiedlichsten Bereichen - Kindermode, Concept Stores, Friseure ) die unser neues Label in Ihr Programm aufnehmen und verkaufen möchten. Wir richten uns mit dem Sortiment von Lunavelle an Mädchen im Alter von 4-11 Jahren. Zum Lunavelle Hair Jewellery Sortiment gehören Haarspangen mit Chiffonblüten, mit decorativen und angesagten Figuren wie Annanas, Eistüten, Flamingos, Muffins, Lamas oder Unicorns mit Glittereffekten sowie Haarclips und Haargummis mit Schleifen aus Baumwollribsbändern in acht verschiedenen Farbvarianten.
Die klassische Haarreifenkollektion besticht durch ihre hochwertige Verarbeitung, elegante Optik und eine große Auswahl an Farbtönen, die sich optimal zu einer Vielzahl von modischen Outfits kombinieren lassen.
Alle Lunavelle Produkte entsprechen den aktuellen Grün Siegel Richtlinien und werden in Handarbeit verarbeitet und konfektioniert.
So werden alle Haarspangen und Clips auf einer Schmuckkarte in einem Klarsichtbeutel liebevoll verpackt und in einem praktischem und emotional ansprechendem Theken Display zum Auffüllen angeboten.
Zur Haarreifenkollektion gehört ebenfalls ein verkaufsförderndendes Theken Display, das die Produkte aufmerksamkeitsstark in den Blickpunkt der Kunden rückt und im unverkennbarem liebevollem Lunavelle Look emotional inszeniert.
Die Lunavelle Hair Jewellery Kollektion ist somit der ideale Mitnahmeartikel für den Kassenbereich im stationären Fach- und Einzelhandel, mit der sich Kunden mit dem Kauf gerne selbst belohnen oder als Impuls für eine schöne Geschenkidee nutzen wollen.
Aufgabenstellung
Auf Basis eines bestehenden Corporate Designs (Logo anbei) und einem Fotoschooting (sehr hochwertiges Bildmaterial sowie einem Layout (Scribble anbei) soll als erstes eine Händlerbroschüre umgesetzt und im Anschluss daran das Layout für eine Website und VKF Materialien (Thekendisplay und Messeposter) adaptiert werden.
Für die Ansprache der Händler dachten wir an eine 24-seitige im Format DinA5 Hoch oder Querformatige Broschüre. Die Broschüre setzt die Kollektion mit besonders hochwertigen Image Bildern in Szene und geht auf die hochwertige Verarbeitung in Form von Produkt Detaillbildern (close up) ein. Die Broschüre soll emotional ansprechen, das liebevolle Design und die hochwertige Verarbeitung zum Ausdruck bringen.
Unser Layoutkonzept sieht folgende Gestaltungs Merkmale vor:
- 1/1 bzw. 2/3 Seite randabfallende Image bzw. Produkt Detailbilder (Close up) mit gegenüberliegendem Text
- Headlines (Begriffe in Englisch), die in groser und ästehtisch ansprechener Typographie ein besonderes Merkmal der Kollektion bzw. der Verarbeitung herausstellen (siehe Scribble)
- Copy Texte die mittelachsig den Bildern gegenüberstehen (Textmanuskript anbei!)
- Farbfelder (Punkte/Kreise) als Inserts , die die unterschiedlichen Farbvarianten bei den Produktdetails (Close up) abbilden
-Poduktabbildungen für die Haarspangen mit Figuren als Inserts!
Gliederung/Struktur der Broschüre: (siehe Scribble)
-Titel Imagebild 1/1 Seite randabfallend + Abbinder (siehe Textmanuskript bzw Scribble)
-Einleitung (Brandstory, Gründergeschichte) Bild Ulrike-Sophie Brandauer mit den Töchtern (Bild folgt im Prozessverlauf)
-Imagebilder bzw Produktbilder (Close up) für 5 Kathegorien (Haarreifen, Haarspangen mit Schleifen, Haarspangen mit Chiffonblüten, Haargummis mit Schliefen, Haarspangen mit Figuren) (Produktbilder folgen im Prozessverlauf)
-Rückseite (Abb VKF Artikel - Displays, Verweis auf Grün Siegel Icon, Anschrift, Kontaktdaten..

```html
<!DOCTYPE html>
<html lang="de">
<head>
<meta charset="utf-8">
<title>Lunavelle Händlerbroschüre</title>
<link href="https://fonts.googleapis.com/css2?family=Great+Vibes&family=Source+Sans+3:wght@400;600&display=swap" rel="stylesheet">
<style>
:root{
  --bg:#e2e2e2;
  --pink:#c23c86;
  --stripe:#ecc7dc;
  --stripe-light:#f6e4ee;
  --teal:#598a95;
  --taupe:#aca399;
  --mist:#e3e5e6;
  --wine:#8f2a36;
  --rose:#d9707f;
  --paper:#ffffff;
  --ink-light:#f2f2f0;
  --grey-script:#b9bcbe;
}
*{margin:0;padding:0;box-sizing:border-box}
html,body{width:1200px;height:3997px;overflow:hidden;background:var(--bg)}
body{position:relative;font-family:"Source Sans 3",sans-serif}
.page,.spread{position:absolute}
.spread{left:225px;width:745px;height:571px;display:flex;box-shadow:0 6px 18px rgba(0,0,0,.18)}
.spread>.leaf{position:relative;width:50%;height:100%;overflow:hidden}
.photo{position:absolute}
.script{font-family:"Great Vibes",cursive;font-weight:400;line-height:1}
.copy{font-size:9.5px;line-height:1.4}

/* cover */
.cover{left:399px;top:112px;width:407px;height:596px;background:var(--paper);box-shadow:0 6px 18px rgba(0,0,0,.2);overflow:hidden}
.cover .photo{left:0;top:0;width:100%;height:480px;background:linear-gradient(180deg,#3d4446 0%,#4a8e9a 45%,#8fa3ad 100%)}
.cover-name{position:absolute;left:0;right:0;top:438px;text-align:center;font-size:72px;font-weight:600;line-height:1;letter-spacing:1px;color:var(--pink)}
.cover-tag{position:absolute;left:0;right:0;top:533px;text-align:center;font-size:14px;font-weight:600;letter-spacing:2.5px;color:var(--pink)}
.cover-rule{position:absolute;left:118px;right:118px;top:554px;border-top:1px solid var(--pink)}
.cover-url{position:absolute;left:0;right:0;top:559px;text-align:center;font-size:12px;letter-spacing:1.6px;color:#777}

/* intro spread */
.intro{top:916px}
.intro .left{background:linear-gradient(90deg,var(--stripe) 0%,var(--stripe-light) 50%,var(--stripe) 100%)}
.intro .left .photo{left:51px;top:50px;width:275px;height:357px;background:linear-gradient(180deg,#2f3436 0%,#4b8d99 40%,#9aa4ab 100%)}
.intro .right{background:var(--teal);color:var(--ink-light);text-align:center}
.head-unique{position:absolute;left:0;right:0;top:108px;font-size:86px;color:#d9e5e8}
.intro .copy-block{position:absolute;left:52px;right:52px;top:205px}
.intro .copy{margin-bottom:9px}
.signature{font-size:17px;margin:6px 0 4px}

/* chick spread */
.chick{top:1715px}
.chick .left .photo{inset:0;background:linear-gradient(180deg,#6b5a3c 0%,#b8b4ad 14%,#c9c6c1 60%,#a9a59f 100%)}
.chick .right{background:var(--taupe);color:var(--ink-light)}
.head-chick{position:absolute;left:48px;top:120px;font-size:104px;color:#ece8e3}
.chick .copy{position:absolute;left:48px;width:200px;top:262px}

/* high-valency spread */
.valency{top:2517px}
.valency .left{background:var(--mist)}
.valency .photo{left:186px;top:0;width:559px;height:100%;background:linear-gradient(120deg,#c9ccce 0%,#d9dcde 40%,#c3c7c9 100%)}
.valency .right .photo{left:-186px}
.head-valency{position:absolute;left:28px;top:40px;font-size:80px;color:var(--grey-script);line-height:.95}
.valency .copy{position:absolute;left:30px;width:150px;top:247px;color:#8a8d8f;font-size:8.5px}
.swatches{position:absolute;left:48px;top:445px;width:210px;display:grid;grid-template-columns:repeat(4,40px);gap:19px 14px}
.swatch{width:40px;height:40px;border-radius:50%}

/* classic spread */
.classic{top:3318px}
.classic .left .photo{inset:0;background:linear-gradient(180deg,#5a6a6a 0%,#d8cbb8 30%,#e7dfd6 70%,#efe9e4 100%)}
.classic .right{background:var(--wine);color:#f1d9dc;text-align:center}
.head-classic{position:absolute;left:0;right:0;top:185px;font-size:98px;color:var(--rose)}
.classic .copy{position:absolute;left:62px;right:62px;top:300px}
</style>
</head>
<body>

<section class="page cover">
  <div class="photo" role="img" aria-label="Titelbild: Mädchen mit weißer Haarschleife vor türkisem Hintergrund"></div>
  <div class="cover-name">Lunavelle</div>
  <div class="cover-tag">UNIQUE HAIRJEWELLERY</div>
  <div class="cover-rule"></div>
  <div class="cover-url">www.lunavelle.de</div>
</section>

<section class="spread intro">
  <div class="leaf left" role="img" aria-label="Rosa-weiß gestreifter Seitenhintergrund mit weißen Sternen">
    <div class="photo" role="img" aria-label="Porträt eines Mädchens mit weißer Schleife im Haar"></div>
  </div>
  <div class="leaf right">
    <h2 class="head-unique script">unique</h2>
    <div class="copy-block">
      <p class="copy">Auf die kleinen Dinge kommt es oft an – diese Erfahrung habe ich als Gründerin von Lunavelle mit einem neuen Label für stilvollen Haarschmuck gemacht.</p>
      <p class="copy">Schnell hat sich gezeigt, dass die stilvollen Designs und die liebevolle Verarbeitung der Haarreifen und Haarspangen bei Müttern und Kindern gut ankommen.</p>
      <p class="copy">Zum Lunavelle Hair Jewellery Sortiment gehören neben Haarreifen auch Haarspangen mit Chiffonblüten, dekorativen Figuren sowie Clips und Bänder in vielen Farbvarianten.</p>
      <p class="copy">Überzeugen Sie sich selbst auf den folgenden Seiten von meiner Kollektion.</p>
      <p class="copy">Ich freue mich auf eine erfolgreiche Zusammenarbeit!</p>
      <p class="signature script">Ulrike-Sophie Brandauer</p>
      <p class="copy">Ihre Ulrike-Sophie Brandauer<br>Dr. Ulrike-Sophie Brandauer</p>
    </div>
  </div>
</section>

<section class="spread chick">
  <div class="leaf left">
    <div class="photo" role="img" aria-label="Zwei Mädchen in grauen Kleidern mit Haarreifen vor goldenem Rahmen"></div>
  </div>
  <div class="leaf right">
    <h2 class="head-chick script">chick</h2>
    <p class="copy">Die Haarreifenkollektion überzeugt durch eine elegante Optik und eine große Auswahl an Farbtönen, die sich optimal zu einer Vielzahl von modischen Outfits kombinieren lassen.</p>
  </div>
</section>

<section class="spread valency">
  <div class="leaf left">
    <div class="photo" role="img" aria-label="Nahaufnahme eines hellgrauen Haarreifens mit Schleife"></div>
    <h2 class="head-valency script">high-<br>valency</h2>
    <p class="copy">Oftmals sind es die kleinen Details, die den Unterschied ausmachen. So bestechen Lunavelle Haarreifen durch die Verwendung hochwertiger Materialien und besonderer Verarbeitung wie z.B. der vierfachen Schleife.</p>
    <div class="swatches">
      <span class="swatch" style="background:#e0b5d0"></span>
      <span class="swatch" style="background:#5f8a93"></span>
      <span class="swatch" style="background:#2a9bc4"></span>
      <span class="swatch" style="background:#e6e7e8"></span>
      <span class="swatch" style="background:#b9427f"></span>
      <span class="swatch" style="background:#1f8fc0"></span>
      <span class="swatch" style="background:#76b55a"></span>
      <span class="swatch" style="background:#8a8a8a"></span>
    </div>
  </div>
  <div class="leaf right">
    <div class="photo" role="img" aria-label="Nahaufnahme eines hellgrauen Haarreifens mit Schleife"></div>
  </div>
</section>

<section class="spread classic">
  <div class="leaf left">
    <div class="photo" role="img" aria-label="Blondes Mädchen in weißem Kleid mit Haarspange und Stoffschwan"></div>
  </div>
  <div class="leaf right">
    <h2 class="head-classic script">classic</h2>
    <p class="copy">Die klassischen Haarspangen von Lunavelle sind zeitlos und verleihen dem Outfit eines Kindes die persönliche Note.</p>
  </div>
</section>

</body>
</html>
```